Business Card Design for Music Therapy Startup

I began my journey attending the Brantwell College School of Music to become a music educator before changing my degree and graduating with a Bachelor's degree in Music with an Outside Field in Psychology in 2008. From there, I attended Dunmore State University where I completed my Bachelor's Equivalency degree in Music Therapy. I became a Board Certified - Music Therapist almost 3 years ago and have since specialized in geriatrics, bereavement and end of life care. I anticipate completing my Master's Degree in Music Therapy in May, 2015, from Kessington State University.

In August of 2014 I completed advanced training in Neurologic Music Therapy (NMT) allowing me to also address speech and language, sensorimotor and cognitive deficits which develop as a result of neurologic injury and disease processes. Parkinson's Disease, Stroke, Traumatic Brain Injury and Dementia are amongst some of the neurologic conditions which may be treated with NMT.

My Philosophy: I strive to provide professional, genuine and compassionate care to all individuals, families and facilities that I serve. I use evidence-based and standardized music-based therapeutic techniques to achieve results which are documented, while complying with privacy regulations. I work with my patients and families to assess the primary goals to be addressed and to establish the most effective treatment plan to facilitate the best results.

Industry/Entity Type

Training

Contact Information for Business Card

Lorena J. Deskow, MT-BC
Neurologic Music Therapist

Riverbend Sound Therapy, LLC

555.204.6617

www.riverbendsoundtherapy.example
riverbendRST@mailbox.example

```html
<!DOCTYPE html>
<html lang="en">
<head>
<meta charset="utf-8">
<title>Riverbend Sound Therapy – Business Card</title>
<link rel="stylesheet" href="https://fonts.googleapis.com/css2?family=Cinzel:wght@400&family=Arimo:wght@400&display=swap">
<style>
  :root {
    --page-bg: #eeeeef;
    --card-white: #fbfbfb;
    --band-black: #000000;
    --brand-blue: #5d90d2;
  }
  * { margin: 0; padding: 0; box-sizing: border-box; }
  html, body {
    width: 1200px;
    height: 864px;
    overflow: hidden;
    background: var(--page-bg);
  }
  .stage {
    width: 1200px;
    height: 864px;
    display: flex;
    align-items: center;
    justify-content: center;
  }
  .business-card {
    width: 840px;
    height: 480px;
    background: var(--card-white);
    box-shadow: 0 10px 30px rgba(0,0,0,0.18);
    display: flex;
    flex-direction: column;
  }
  .brand-band {
    height: 190px;
    background: var(--band-black);
    display: flex;
    align-items: flex-end;
    justify-content: center;
    padding-bottom: 42px;
    gap: 16px;
  }
  .brand-mark {
    width: 18px;
    height: 18px;
    border-radius: 50%;
    background: var(--brand-blue);
    margin-bottom: 10px;
  }
  .brand-name {
    font-family: "Cinzel", serif;
    font-weight: 400;
    font-size: 38px;
    color: var(--brand-blue);
    letter-spacing: 0.5px;
  }
  .card-body {
    flex: 1;
    text-align: center;
    color: var(--brand-blue);
    padding-top: 26px;
  }
  .person-name {
    font-family: "Cinzel", serif;
    font-size: 27px;
    letter-spacing: 1.5px;
    line-height: 1.2;
  }
  .person-title {
    font-family: "Arimo", sans-serif;
    font-size: 19px;
    margin-top: 4px;
  }
  .contact-list {
    list-style: none;
    font-family: "Arimo", sans-serif;
    font-size: 19px;
    line-height: 1.75;
    margin-top: 42px;
  }
</style>
</head>
<body>
  <main class="stage">
    <article class="business-card">
      <header class="brand-band">
        <span class="brand-mark" aria-hidden="true"></span>
        <span class="brand-name">Riverbend Sound Therapy, LLC</span>
      </header>
      <section class="card-body">
        <h1 class="person-name">Lorena J. Deskow, MT-BC</h1>
        <p class="person-title">Neurologic Music Therapist</p>
        <ul class="contact-list">
          <li class="contact-phone">555.204.6617</li>
          <li class="contact-web">www.riverbendsoundtherapy.example</li>
          <li class="contact-email">lorena@riverbendsoundtherapy.example</li>
        </ul>
      </section>
    </article>
  </main>
</body>
</html>
```